Custom Truck shop New Business Card design

double sided business card including my new logo, brand colors and picking a font I attached, clean and modern look. I attached the old card for some reference. and would like to include the picture of the white truck attached. I would also like to have it with one of my employees info as well. (same info except name and title Brin Tolvay Service Writer)

Dale Porvick
Owner

address
48310 E Calloway Ridge Rd S
STE 217
Marsh Hollow, CO 80219

phone 720-555-0184

email dale@brokenspurrigs.example

website brokenspurrgis.example

social @brokenspurrigs

Target Market(s)

men 18-60

Industry/Entity Type

Automotive

Contact Information for Business Card

Dale Porvick Owner address 48310 E Calloway Ridge Rd S STE 217 Marsh Hollow, CO 80219 phone 720-555-0184 email dale@brokenspurrigs.example website brokenspurrgis.example social @brokenspurrigs

Font styles to use
Other font styles liked:
• fonts attached

Requirements
Must have
• new logo, orange #FC68D, Charcoal #333333
Nice to have
• the white truck

```html
<!DOCTYPE html>
<html lang="en">
<head>
<meta charset="utf-8">
<title>Broken Spur Rigs – Business Card</title>
<link rel="stylesheet" href="https://fonts.googleapis.com/css2?family=Arimo:wght@400;700&display=swap">
<style>
  :root {
    --orange: #ff6a13;
    --orange-soft: #ff6b2c;
    --charcoal: #333333;
    --white: #ffffff;
    --backdrop: #e9e9e9;
  }
  * { box-sizing: border-box; margin: 0; padding: 0; }
  html, body {
    width: 1200px; height: 874px; overflow: hidden;
    background: var(--backdrop);
    font-family: "Arimo", Arial, sans-serif;
  }
  .canvas {
    width: 1200px; height: 874px;
    display: flex; flex-direction: column; align-items: center; justify-content: center;
    gap: 30px;
  }
  .card {
    width: 680px; height: 389px;
    border-radius: 22px;
    position: relative; overflow: hidden;
    box-shadow: 0 6px 18px rgba(0,0,0,.18);
  }

  /* Front */
  .card-front { background: var(--orange); color: var(--white); }
  .front-mark {
    position: absolute; left: 0; right: 0; top: 120px;
    display: flex; align-items: center; justify-content: center; gap: 16px;
  }
  .front-mark .dot {
    width: 46px; height: 46px; border-radius: 50%;
    border: 4px solid var(--white);
  }
  .front-mark .brand-name {
    font-weight: 700; font-size: 40px; letter-spacing: 1px; text-transform: uppercase;
  }
  .social {
    position: absolute; left: 0; right: 0; bottom: 62px;
    display: flex; align-items: center; justify-content: center; gap: 10px;
    font-size: 19px;
  }
  .social .dot { width: 16px; height: 16px; border-radius: 50%; background: var(--white); }

  /* Back */
  .card-back { background: var(--orange-soft); color: var(--white); }
  .back-top {
    position: absolute; left: 0; right: 0; top: 0; height: 180px;
    background: var(--white);
    display: flex; align-items: center; justify-content: center; gap: 14px;
  }
  .back-top .dot { width: 42px; height: 42px; border-radius: 50%; background: var(--charcoal); }
  .back-top .brand-name {
    color: var(--charcoal); font-weight: 700; font-size: 38px; letter-spacing: 1px;
    text-transform: uppercase;
  }
  .divider-band {
    position: absolute; left: 0; right: 0; top: 180px; height: 7px; background: var(--charcoal);
  }
  .person {
    position: absolute; top: 226px; right: 372px; text-align: right;
  }
  .person .name { font-weight: 700; font-size: 28px; }
  .person .title { font-size: 17px; margin-top: 2px; }
  .rule {
    position: absolute; left: 340px; top: 218px; width: 1px; height: 118px;
    background: var(--white);
  }
  .contact {
    position: absolute; left: 362px; top: 214px;
    font-size: 17px; line-height: 1.28;
  }
  .contact .address { margin-bottom: 6px; }
  .contact .row { display: flex; align-items: center; gap: 9px; }
  .contact svg { width: 14px; height: 14px; flex: none; }
</style>
</head>
<body>
<main class="canvas">
  <section class="card card-front">
    <div class="front-mark">
      <span class="dot"></span>
      <span class="brand-name">Broken Spur Rigs</span>
    </div>
    <div class="social">
      <span class="dot"></span>
      <span class="handle">@brokenspurrigs</span>
    </div>
  </section>

  <section class="card card-back">
    <header class="back-top">
      <span class="dot"></span>
      <span class="brand-name">Broken Spur Rigs</span>
    </header>
    <div class="divider-band"></div>

    <div class="person">
      <p class="name">Dale Porvick</p>
      <p class="title">Managing Director</p>
    </div>
    <div class="rule"></div>

    <div class="contact">
      <p class="address">48310 E Calloway Ridge Rd S<br>STE 217, Marsh Hollow, CO 80219</p>
      <p class="row">
        <svg viewBox="0 0 24 24" fill="#fff"><path d="M6.6 10.8a15.1 15.1 0 0 0 6.6 6.6l2.2-2.2c.3-.3.7-.4 1-.2 1.1.4 2.3.6 3.6.6.6 0 1 .4 1 1V20c0 .6-.4 1-1 1A17 17 0 0 1 3 4c0-.6.4-1 1-1h3.5c.6 0 1 .4 1 1 0 1.3.2 2.5.6 3.6.1.3 0 .7-.2 1z"/></svg>
        <span>720-555-0184</span>
      </p>
      <p class="row">
        <svg viewBox="0 0 24 24" fill="#fff"><path d="M2 5h20v14H2zM3.5 6.5 12 12.5l8.5-6H3.5z"/></svg>
        <span>dale@brokenspurrigs.example</span>
      </p>
      <p class="row">
        <svg viewBox="0 0 24 24" fill="none" stroke="#fff" stroke-width="2"><circle cx="12" cy="12" r="9"/><path d="M3 12h18M12 3c3 3.5 3 14.5 0 18M12 3c-3 3.5-3 14.5 0 18"/></svg>
        <span>www.brokenspurrigs.example</span>
      </p>
    </div>
  </section>
</main>
</body>
</html>
```